Stationery Design Project for Marketing Consultancy

I have started a new consultancy business and require the following elements to be designed using existing logo:
• Business card
• Letterhead
• Envelope (DL, C4, C5)
• Microsoft word template for report writing
• A4 Presentation Folder
• Powerpoint template
COPY FOR FRONT AND BACK OF BUSINESS CARD
logo
'Countable Growth. Bold Outcomes' slogan (but no need to use existing lockup with logo)
name, B Bus. Mktg, Grad Dip Digital Mktg, CPM (post nominal abbreviations in smaller font)
mobile: 04XX-XXX-XXX (I will give details to the winner to add)
website: www.quorvale.com.au
email: info@quorvale.com.au
COPY FOR LETTERHEAD
Logo
Company Name
Please, submit your designs that include business card, letterhead and envelope. Once selected the winner will be asked to complete the project by creating the rest of the artwork.
FINAL FILES
Print ready files to be supplied as well as Indesign files so that minor amends can be made if necessary in future.
• Layered vectors in EPS & PDF
• Screen quality JPEG & PNGs
ABOUT THE BUSINESS: QUORVALE
I work with clients to understand their business challenges, developing and executing measurable marketing strategies tied to key business metrics. Services include:
Services include:
• Business planning and business development
• Marketing and brand strategy
• Insight-driven integrated campaigns
• Loyalty programs and retention marketing
• Marketing automation
• Direct marketing (traditional and digital)
• Content strategy and development
Hi everyone,
Target Market(s)
Corporate decision makers (heads of marketing, general managers etc) and small to medium sized business owners. Predominately male aged 35+
Industry/Entity Type
Marketing
Requirements
Must have
- BRAND PERSONALITY
The successful design will communicate brand personality. I am a professional, results-driven entrepreneur, but want to show off my creative flair.
MEMORABILITY
Looking for a unique and eye-catching design. Am considering special printing effects (die cuts, letterpress, interactive elements, embossing, foiling etc) or a striking minimalist approach.
Nice to have
- I have a mission that could be incorporated on reverse if room -
Turning insights into actions & passion into profit.
Should not have
- Use of pink or green.

```html
<!DOCTYPE html>
<html lang="en">
<head>
<meta charset="utf-8">
<title>Quorvale Business Card</title>
<link rel="stylesheet" href="https://fonts.googleapis.com/css2?family=Montserrat:wght@400;500;600;700&display=swap">
<style>
  :root {
    --backdrop: #d9dadb;
    --card: #f4f4f2;
    --ink: #33434f;
    --brand-blue: #2a6c95;
    --rule: #3b4a55;
  }
  * { margin: 0; padding: 0; box-sizing: border-box; }
  html, body {
    width: 1200px;
    height: 1005px;
    overflow: hidden;
    background: var(--backdrop);
    font-family: "Montserrat", Arial, sans-serif;
    color: var(--ink);
  }
  .business-card {
    position: absolute;
    left: 100px;
    top: 197px;
    width: 1000px;
    height: 611px;
    background: var(--card);
    box-shadow: 0 6px 24px rgba(0,0,0,0.12);
  }
  .brand-lockup {
    position: absolute;
    left: 120px;
    top: 262px;
    display: flex;
    align-items: center;
    gap: 18px;
  }
  .brand-dot {
    width: 50px;
    height: 50px;
    border-radius: 50%;
    background: var(--brand-blue);
  }
  .brand-name {
    font-size: 54px;
    font-weight: 600;
    color: var(--brand-blue);
    letter-spacing: 1px;
    line-height: 1;
  }
  .divider {
    position: absolute;
    left: 530px;
    top: 145px;
    width: 2px;
    height: 230px;
    background: var(--rule);
  }
  .contact-block {
    position: absolute;
    left: 575px;
    top: 148px;
  }
  .person-name {
    font-size: 24px;
    font-weight: 500;
    letter-spacing: 1px;
    text-transform: uppercase;
    margin-bottom: 16px;
  }
  .credentials {
    font-size: 15px;
    font-weight: 500;
    line-height: 28px;
    margin-bottom: 40px;
  }
  .contact-list { list-style: none; }
  .contact-list li {
    font-size: 17px;
    font-weight: 400;
    line-height: 33px;
  }
  .contact-label {
    display: inline-block;
    width: 24px;
    font-weight: 700;
    color: var(--brand-blue);
  }
  .tagline {
    position: absolute;
    left: 0;
    right: 0;
    top: 476px;
    text-align: center;
    font-size: 23px;
    font-weight: 400;
    letter-spacing: 1.5px;
    text-transform: uppercase;
  }
  .tagline strong { font-weight: 600; }
</style>
</head>
<body>
  <main class="business-card">
    <div class="brand-lockup">
      <span class="brand-dot"></span>
      <span class="brand-name">QUORVALE</span>
    </div>

    <div class="divider"></div>

    <section class="contact-block">
      <h1 class="person-name">Daniel Harwood</h1>
      <p class="credentials">B Bus. Mktg,<br>Grad Dip Digital Mktg, CPM</p>
      <ul class="contact-list">
        <li><span class="contact-label">M</span>0400-555-217</li>
        <li><span class="contact-label">E</span>info@quorvale.com.au</li>
        <li><span class="contact-label">W</span>www.quorvale.com.au</li>
      </ul>
    </section>

    <p class="tagline">Countable Growth. <strong>Bold Outcomes.</strong></p>
  </main>
</body>
</html>
```